New Bottle Label for our Velmoris Grand Reserva Brandy

Graphic Design Brief
We need a new bottle label for our Brandy Gran Reserva that we want to bring to the market.
Please have a look at all our current bottles and labels and the feel of our company under www.velmoris-distill.ch. We would like the design to be still different to the rest - as it is not a whisky, not a fruit product, not a spirit like a gin, thus we need to create like a new family, but still fitting in with the rest of the products.
The bottle that we will be using for the brand is a different one than the one that we already have, the design of the bottle is attached with a document.
I have also attached a briefing in regards to Brandy in general for your information.
### 1. What is Brandy?
Brandy is a distilled spirit made from fermented wine or other fruit wines. It is traditionally aged in oak barrels, which gives it its characteristic color and rich flavor. The aging process in oak is essential for developing the aromas and quality of the brandy.
### 2. What is Brandy Reserva?
A Brandy labeled as "Reserva" has undergone a longer aging process, typically at least 2 to 3 years, in oak barrels. This aging gives the brandy a deeper, more complex flavor profile and a darker color. "Reserva" is often an indication of higher quality.
### 3. Who enjoys drinking Brandy?
Brandy is typically favored by those who appreciate a deep, rich tasting experience. This often includes older consumers who value the time-aged complexity of the spirit. However, Brandy is also gaining popularity among younger people, especially through cocktails and modern serving styles.
### 4. Why is Brandy trending?
Brandy is experiencing a resurgence as consumers increasingly value quality and artisanal production methods. Its versatility in cocktails and association with traditional, luxurious experiences have also contributed to its renewed popularity.
### 5. What colors would be associated with Brandy?
The typical colors associated with Brandy are warm gold, amber, and deep golden-brown tones. These colors reflect the aging process in oak barrels and the richness of the flavors. Other associated colors might include dark brown and mahogany.
### 6. What is important to customers when buying Brandy?
Customers care about the origin of the Brandy, the aging time, the quality of the ingredients, the production method, and the brand. They also pay attention to the prestige of the product and the authenticity of the production.
### 7. What is not important to customers when buying Brandy?
For many customers, the price and packaging (unless it’s especially exclusive) may be less important than the quality and taste of the Brandy. The distillery name might be less significant if it isn’t tied to a particular reputation.
### 8. What do customers know about Swiss Brandy?
Swiss Brandy is still relatively unknown in many markets, but customers who are familiar with it appreciate the precision and quality of Swiss production. Swiss Brandy is assumed to be made with care and under strict quality standards.
### 9. What is Brandy Gran Reserva?
**Brandy Gran Reserva** is an even higher quality and longer-aged version of Brandy. Generally, a Gran Reserva is aged for at least 5 to 10 years or more in oak barrels. This extended aging process gives the Brandy an especially deep, complex flavor profile and often a darker, richer color. Gran Reserva is often regarded as the top-tier product within a Brandy range and appeals to discerning consumers who value quality, refinement, and a luxurious tasting experience.
The label “Gran Reserva” thus indicates the highest quality level for Brandies, similar to other spirits (like wine or whisky), where the aging time is a critical factor.
We age our Brandy Gran Reserva in the Solara way.
### 10. What emotions are associated with Brandy?
Brandy is often associated with luxury, relaxation, and comfort. It evokes feelings of tradition, elegance, and sophistication. Drinking Brandy is frequently seen as a moment of reflection and enjoyment.
### 11. How should Brandy be marketed?
Brandy should be marketed with a focus on its artisanal production, quality, and tradition. A narrative around the product, its aging, and origin can help create an emotional connection with the customer. The marketing should also emphasize the versatility of Brandy, whether consumed neat or in cocktails.
**Label design**:
The label should reflect the exclusivity of the product, with an elegant, minimalist design. The label should include information about the aging time, the use of oak barrels, and a brief story about the Brandy’s production.
we would like to have a modern look to the whole deisgn of the brandy
Customers that like Brandy
Switzerland
Distillery

```html
<!DOCTYPE html>
<html lang="en">
<head>
<meta charset="utf-8">
<title>Velmoris Brandy Gran Reserva – Bottle Label</title>
<link rel="stylesheet" href="https://fonts.googleapis.com/css2?family=Playfair+Display:wght@600;700&family=EB+Garamond:wght@400;500&display=swap">
<style>
  :root {
    --page: #ffffff;
    --label-black: #0b0b0b;
    --label-panel: #121212;
    --gold-light: #d9cfa0;
    --gold: #b3a676;
    --gold-dark: #6f6642;
    --white: #ffffff;
    --cream: #e3ddd3;
    --ink: #1c1c1c;
  }
  * { margin: 0; padding: 0; box-sizing: border-box; }
  html, body {
    width: 1200px; height: 1200px; overflow: hidden;
    background: var(--page);
  }
  .canvas { position: relative; width: 1200px; height: 1200px; }

  .label {
    position: absolute; left: 290px; top: 92px;
    width: 622px; height: 1022px;
    background: var(--label-black);
    box-shadow: 4px 6px 6px rgba(0,0,0,0.35);
  }
  .frame-outer {
    position: absolute; inset: 13px;
    border: 5px solid var(--gold);
    border-image: linear-gradient(90deg, var(--gold-light), var(--gold), var(--gold-dark), var(--gold-light)) 1;
  }
  .panel {
    position: absolute; inset: 28px;
    background: repeating-linear-gradient(0deg, #151515 0 2px, #101010 2px 4px);
    border: 2px solid var(--gold);
  }

  .ornament {
    position: absolute; top: 64px; width: 104px; height: 128px;
    background: radial-gradient(ellipse at center, rgba(179,166,118,0.35), rgba(179,166,118,0) 70%);
  }
  .ornament--left { left: 36px; }
  .ornament--right { right: 36px; }

  .brand-name {
    position: absolute; left: 0; right: 0; top: 118px;
    text-align: center;
    font-family: "Playfair Display", Georgia, serif;
    font-weight: 700; font-size: 78px; line-height: 1;
    color: var(--white);
  }

  .diamond-row {
    position: absolute; left: 50%; transform: translateX(-50%);
    background: linear-gradient(90deg, var(--gold-light), var(--gold), var(--gold-light));
    opacity: 0.85;
  }
  .diamond-row--top { top: 333px; width: 164px; height: 20px; }
  .diamond-row--bottom { top: 805px; width: 70px; height: 12px; }

  .product-type {
    position: absolute; left: 0; right: 0; top: 432px;
    text-align: center;
    font-family: "Playfair Display", Georgia, serif;
    font-weight: 700; font-size: 84px; line-height: 1; letter-spacing: 6px;
    background: linear-gradient(90deg, #9d925f, var(--gold-light) 45%, #7c7248 70%, var(--gold-light));
    -webkit-background-clip: text; background-clip: text;
    color: transparent;
  }

  .grade-band {
    position: absolute; left: 132px; width: 362px; top: 542px; height: 66px;
    background:
      repeating-linear-gradient(0deg, rgba(217,207,160,0.55) 0 1px, transparent 1px 4px);
    -webkit-mask-image: linear-gradient(90deg, transparent, #000 20%, #000 80%, transparent);
    mask-image: linear-gradient(90deg, transparent, #000 20%, #000 80%, transparent);
  }
  .grade-title {
    position: absolute; left: 0; right: 0; top: 554px;
    text-align: center;
    font-family: "Playfair Display", Georgia, serif;
    font-weight: 600; font-size: 34px; letter-spacing: 2px; line-height: 1.2;
    color: var(--white);
    text-shadow: 1px 1px 0 #000, -1px 0 0 #555;
  }

  .age-badge { position: absolute; left: 261px; top: 678px; width: 100px; height: 100px; }

  .info-box {
    position: absolute; left: 74px; top: 857px; width: 480px; height: 107px;
    background: var(--cream);
  }
  .info-table {
    position: absolute; left: 12px; top: 8px; width: 459px; height: 91px;
    border: 3px solid var(--ink);
    font-family: "EB Garamond", Georgia, serif; color: var(--ink);
  }
  .info-title {
    height: 29px; border-bottom: 1px solid var(--ink);
    text-align: center; font-size: 23px; letter-spacing: 2px; line-height: 30px;
    padding-right: 22px;
  }
  .info-batch { position: absolute; left: 14px; top: 34px; font-size: 16px; }
  .info-side {
    position: absolute; right: 0; top: 29px; bottom: 0; width: 137px;
    border-left: 1px solid var(--ink);
  }
  .info-cell { height: 50%; text-align: center; font-size: 17px; line-height: 28px; }
  .info-cell + .info-cell { border-top: 1px solid var(--ink); }
</style>
</head>
<body>
<div class="canvas">
  <div class="label">
    <div class="frame-outer"></div>
    <div class="panel">
      <div class="ornament ornament--left" role="img" aria-label="Gold filigree corner flourish"></div>
      <div class="ornament ornament--right" role="img" aria-label="Gold filigree corner flourish"></div>

      <div class="brand-name">Velmoris</div>

      <div class="diamond-row diamond-row--top" role="img" aria-label="Two rows of small gold diamond ornaments"></div>

      <div class="product-type">BRANDY</div>

      <div class="grade-band"></div>
      <div class="grade-title">GRAN RESERVA</div>

      <svg class="age-badge" viewBox="0 0 100 100" aria-label="Aged 8 years">
        <defs>
          <linearGradient id="badgeGold" x1="0" y1="0" x2="1" y2="1">
            <stop offset="0" stop-color="#e8dfb4"/>
            <stop offset="0.5" stop-color="#b9ab72"/>
            <stop offset="1" stop-color="#d9cfa0"/>
          </linearGradient>
        </defs>
        <polygon points="50,2 88,20 98,61 72,97 28,97 2,61 12,20" fill="url(#badgeGold)" stroke="#8a7f52" stroke-width="1.5"/>
        <text x="50" y="58" text-anchor="middle" font-family="Playfair Display, Georgia, serif" font-weight="700" font-size="50" fill="#3a3024">8</text>
        <text x="50" y="83" text-anchor="middle" font-family="Playfair Display, Georgia, serif" font-weight="600" font-size="12" fill="#3a3024">AGED YEARS</text>
      </svg>

      <div class="diamond-row diamond-row--bottom" role="img" aria-label="Two small rows of gold diamond ornaments"></div>
    </div>

    <div class="info-box">
      <div class="info-table">
        <div class="info-title">MATURED IN OAK CASKS</div>
        <div class="info-batch">BATCH No.</div>
        <div class="info-side">
          <div class="info-cell">42% abv</div>
          <div class="info-cell">700 ml</div>
        </div>
      </div>
    </div>
  </div>
</div>
</body>
</html>
```